Spa Brochure/service menu for existing spa for men and women

We need a brochure redesign to match our new logo, and business cards. Please keep in mind we love simplicity and no orchids. Tri-fold. unique. simple. eye catching front. Brochure serves as service menu in and out of business. Our clientel base is equal parts men and women. We are a privately owned and very unique business and would like our brochure to reflect that.

Target Market(s)

Men and women between 30- 65 from the greater NY area on a getaway in our quaint town

Industry/Entity Type

Business

Other font styles liked:
• Avalon. Anything that compliments current fonts in print and logo

Requirements
Must have
• Black, White and Gold design sticking with our new business cards (see attachement). Straight forward and clean. Our biggest concern is the front page being clean and appealing. (open to ideas) Logo on front page as main focus, design in background to highlight it a plus.
Nice to have
• Unique design. A simple map of our location in relation to Main Street and the ski slope on back page. Snail design featured.
Should not have
• No orchids. We hate orchids. No overly feminine tones. No generic spa images etc.

```html
<!DOCTYPE html>
<html lang="en">
<head>
<meta charset="utf-8">
<title>Spa Service Menu</title>
<link href="https://fonts.googleapis.com/css2?family=Questrial&display=swap" rel="stylesheet">
<style>
  :root {
    --paper: #ffffff;
    --paper-warm: #f6f3ec;
    --gold: #b8964f;
    --ink: #111111;
    --ink-soft: #2a2a2a;
  }
  * { margin: 0; padding: 0; box-sizing: border-box; }
  html, body { width: 1200px; height: 849px; overflow: hidden; }
  body {
    font-family: "Questrial", "Century Gothic", sans-serif;
    color: var(--ink);
    background: linear-gradient(160deg, var(--paper) 0%, var(--paper) 50%, var(--paper-warm) 100%);
    position: relative;
  }
  .dot {
    position: absolute; width: 14px; height: 14px; border-radius: 50%;
    background: var(--gold);
  }
  .rule { position: absolute; width: 1px; background: var(--gold); }
  .section-title {
    position: absolute; font-size: 48px; line-height: 1; color: var(--gold);
    writing-mode: vertical-rl; transform: rotate(180deg); white-space: nowrap;
  }
  .service { position: absolute; }
  .service h3 {
    font-weight: 400; font-size: 19px; line-height: 22px; color: var(--ink);
    position: relative; white-space: nowrap;
  }
  .service h3::before {
    content: ""; position: absolute; left: -9px; top: 10px;
    width: 3px; height: 3px; border-radius: 50%; background: var(--gold);
  }
  .service h3 small { font-size: 15px; }
  .service p {
    font-size: 12.4px; line-height: 16px; color: var(--ink-soft); margin-top: 4px;
    white-space: nowrap;
  }
  .col-left .service { left: 81px; }
  .col-mid .service { left: 467px; }
  .col-right .service { left: 880px; }
  .footer { position: absolute; display: flex; align-items: flex-end; top: 796px; }
  .footer .line { width: 128px; height: 1px; background: var(--gold); margin-right: 13px; margin-bottom: 14px; }
  .footer span { font-size: 11px; color: var(--ink-soft); margin-right: 6px; margin-bottom: 3px; }
  .footer .mark {
    width: 24px; height: 24px; border-radius: 50%; background: var(--gold);
  }
</style>
</head>
<body>

<section class="col-left">
  <div class="dot" style="left:30px; top:29px;"></div>
  <div class="rule" style="left:37px; top:36px; height:473px;"></div>
  <div class="section-title" style="left:13px; top:519px;">Massages</div>

  <div class="service" style="top:26px;"><h3>Swedish</h3>
    <p>Relaxing and therapeutic.<br>Ease tension and enhance circulation.<br>Great for a first time massage or any spa<br>veteran.</p></div>
  <div class="service" style="top:133px;"><h3>Deep Tissue</h3>
    <p>A therapeutic combination of slow and<br>deep pressure alleviates chronic pain,<br>muscle fatigue, and limited range of motion.<br>Muscle Therapy lotion or creme.</p></div>
  <div class="service" style="top:245px;"><h3>Tension Tamer</h3>
    <p>Head, neck and shoulders.<br>Deep Tissue with towels, muscle soothing oils,<br>and cups.</p></div>
  <div class="service" style="top:342px;"><h3>Hot Stone</h3>
    <p>Unforgettable.<br>Warm basalt lava stones melt away all stress<br>and tensions in sore muscles and joints.<br>The ultimate Aprés ski treat.</p></div>
  <div class="service" style="top:454px;"><h3>Recovery</h3>
    <p>Specific to your athletic needs,<br>whether pro or a weekend warrior.<br>Relax, stretch and recover.</p></div>
  <div class="service" style="top:550px;"><h3>Synergy</h3>
    <p>East meets West. Old meets new.<br>A therapeutic blend of cupping, hot stone,<br>Ayurvedic kansa and Italian Marble rolling.</p></div>
  <div class="service" style="top:657px;"><h3>Prenatal</h3>
    <p>Ultimate treat for Mother-to-be.<br>Soothes aches and pains during pregnancy.<br>Mother must be out of 1st trimester.</p></div>

  <div class="footer" style="left:72px;">
    <div class="line"></div><span>Slow down. Enjoy life</span>
    <div class="mark" role="img" aria-label="Small snail emblem"></div>
  </div>
</section>

<section class="col-mid">
  <div class="section-title" style="left:409px; top:25px;">Facials</div>
  <div class="dot" style="left:426px; top:185px;"></div>
  <div class="rule" style="left:433px; top:192px; height:627px;"></div>

  <div class="service" style="top:26px;"><h3>Seasonal</h3>
    <p>Call spa concierge for details.</p></div>
  <div class="service" style="top:78px;"><h3>Healing Manuka Honey</h3>
    <p>A must for dull, dry or damaged skin.<br>Relieves facial tension, hydrates and plumps.</p></div>
  <div class="service" style="top:150px;"><h3>Age-Defying Facial</h3>
    <p>Our organic detox firming peel resurfaces,<br>hydrates and delivers vital nutrients for younger,<br>healthier skin.</p></div>
  <div class="service" style="top:235px;"><h3>Arctic Berry illuminating Facial</h3>
    <p>Replenish and restore elasticity. Top of the line<br>Organic peel with minimum reaction and<br>maximum results. All organic.</p></div>
  <div class="service" style="top:325px;"><h3>Vitamin C</h3>
    <p>Ideal for all skin types. Potent Vitamin C &amp; E<br>reduces appearance of sun damage, fine lines<br>and wrinkles. Organic and revolutionary stable<br>Vitamin C.</p></div>
  <div class="service" style="top:424px;"><h3>Deep Cleansing</h3>
    <p>A deeper clean with clarifying enzymes and<br>vacuum extraction. Won't aggravate sensitive<br>and temperamental skin.</p></div>
  <div class="service" style="top:512px;"><h3>Clear Skin</h3>
    <p>Cleanse and clarify problem skin with the power<br>of organic tea tree oil, alpha hydroxy acid and<br>cucumber. Healing probiotics help precent future<br>breakouts and treat blemished, inflamed skin.</p></div>
  <div class="service" style="top:614px;"><h3>Microdermabrasion</h3>
    <p>Reduce wrinkles, scarring, discoloration, sun<br>damage, large pores and age spots. Stimulate<br>collagen and elastin production through diamond<br>and crystal exfoliation. Best in series of six.<br>(Immediately reveal younger smoother skin.<br>Dramatically reduce).</p></div>
  <div class="service" style="top:749px;"><h3>Calm Skin <small>(Rosacea and Sensitive Skin)</small></h3>
    <p>Soothe and balance the complexion. Reduce<br>irritation and redness with chamomile and arnica,<br>while hydrating and healing.</p></div>
</section>

<section class="col-right">
  <div class="dot" style="left:831px; top:29px;"></div>
  <div class="rule" style="left:838px; top:36px; height:304px;"></div>
  <div class="section-title" style="left:814px; top:350px;">Hand &amp; Foot Care</div>

  <div class="service" style="top:26px;"><h3>Petitie Manicure</h3>
    <p>Snip, clip, file, polish and voile.</p></div>
  <div class="service" style="top:94px;"><h3>Classic Manicure</h3>
    <p>A warm soak, hand and arm massage, nail<br>shaping and cuticle care followed by your<br>choice of enamel.</p></div>
  <div class="service" style="top:195px;"><h3>French Manicure +$5</h3></div>
  <div class="service" style="top:245px;"><h3>Hollow Creek Manicure</h3>
    <p>In addition to a Classic manicure, a gentle<br>exfoliation, soothing masque and hydrating<br>Sedona mud &amp; paraffin dip. Relax, baby<br>soft, beautiful.</p></div>
  <div class="service" style="top:364px;"><h3>Classic Pedicure</h3>
    <p>Green tea foot soak, peppermint exfoliation<br>foot scrub, massage, nail care and polish.</p></div>
  <div class="service" style="top:451px;"><h3>French Pedicure +10</h3></div>
  <div class="service" style="top:498px;"><h3>Hollow Creek Pedicure</h3>
    <p>In addition to a classic pedicure, a soothing<br>anti-inflammatory mud mask and revitalizing<br>foot, calf massage, Sedona mud paraffin<br>treatment. Topped off with your choice of<br>enamel</p></div>
  <div class="service" style="top:622px;"><h3>Apothecary-Pedi</h3>
    <p>Create your one of a kind Pedicure<br>experience. A consultation, creation and<br>service to match a person as unique as you.<br>Bespoke soak, scrub and masque.<br>Includes nail care, massage, and enamel.</p></div>

  <div class="footer" style="left:883px;">
    <div class="line"></div><span>Slow down. Enjoy life</span>
    <div class="mark" role="img" aria-label="Small snail emblem"></div>
  </div>
</section>

</body>
</html>
```